Web Design for Financial Consulting Company

We need a website design for a financial consulting company "Kelvane Consulting". We build financial models, scenario analysis, handle the budgeting process and provide temporary staffing. I have over 10 years of experience. My Excel expertise and analytical savvy has saved clients over $17 million in profit.

Target Market(s)

Small to medium businesses

Industry/Entity Type

Financial Consulting

Number of Pages Required

4 page

Requirements
Must have
• Professional looking
Nice to have
• A little futuristic looking

```html
<!DOCTYPE html>
<html lang="en">
<head>
<meta charset="utf-8">
<title>Kelvane Consulting</title>
<link rel="stylesheet" href="https://fonts.googleapis.com/css2?family=Poppins:wght@400;500;600;700;800&display=swap">
<style>
:root{
  --navy:#16222d;
  --navy-card:#1e2d3b;
  --navy-field:#111b23;
  --navy-dot:#0f1820;
  --blue:#00aaf0;
  --white:#ffffff;
  --ink:#16222d;
  --mist:#e9ecef;
}
*{margin:0;padding:0;box-sizing:border-box}
html,body{width:720px;height:1200px;overflow:hidden}
body{font-family:'Poppins',sans-serif;background:var(--navy);color:var(--white);position:relative}
.abs{position:absolute}

/* header */
.brand{left:89px;top:16px;display:flex;align-items:center;gap:6px}
.brand-square{width:16px;height:16px;border:2px solid var(--blue)}
.brand-name{font-weight:600;font-size:11px;letter-spacing:1.2px;color:var(--white);text-transform:uppercase}
.nav{top:15px;left:440px;display:flex;gap:0}
.nav a{color:var(--white);text-decoration:none;font-weight:600;font-size:6.6px;padding-top:5px;margin-right:16px;border-top:1.5px solid transparent}
.nav a.active{color:var(--blue);border-top-color:var(--blue);padding-left:5px;padding-right:5px;margin-left:-5px;margin-right:11px}

/* hero */
.hero-photo{left:340px;top:46px;width:310px;height:248px;background:radial-gradient(ellipse at 55% 45%,#6c747b 0%,#3a434b 45%,#1b2630 80%);border-radius:120px 120px 0 0}
.hero-title{left:87px;top:114px;font-weight:800;font-size:26.5px;line-height:30.5px;text-transform:uppercase}
.btn-outline{left:87px;top:218px;width:86px;height:25px;border:1.5px solid var(--blue);color:var(--white);font-weight:700;font-size:8.8px;display:flex;align-items:center;justify-content:center}

/* band behind services */
.desk-band{left:0;top:382px;width:720px;height:140px;background:linear-gradient(100deg,#dfe2e5 0%,#f2f3f4 45%,#e4e6e8 100%)}

/* services */
.service{top:294px;width:114px;height:133px;background:var(--navy-card);padding:16px 11px 0 11px}
.service.featured{background:var(--blue)}
.service svg{display:block;height:22px;margin-bottom:12px}
.service h3{font-weight:700;font-size:7.8px;line-height:9.6px;text-transform:uppercase;margin-bottom:7px}
.service p{font-size:6.6px;line-height:7.8px}

/* about */
.about-photo{left:0;top:521px;width:365px;height:245px;background:linear-gradient(90deg,#4e575e 0%,#8d959b 45%,#c9d0d5 80%,#b6bec4 100%)}
.about-panel{left:365px;top:484px;width:355px;height:303px;background:var(--white)}
.about-title{left:403px;top:538px;color:var(--ink);font-weight:800;font-size:25px;line-height:30px}
.about-text{left:403px;top:580px;width:243px;color:var(--ink);font-size:6.4px;line-height:7.8px}
.btn-dark{left:588px;top:621px;width:62px;height:15.5px;background:var(--ink);color:var(--white);font-weight:700;font-size:7px;display:flex;align-items:center;justify-content:center;box-shadow:0 6px 14px rgba(0,0,0,.12)}
.about-illustration{left:405px;top:643px;width:196px;height:134px;background:linear-gradient(180deg,#f3f5f7 0%,#dfe5ea 100%)}

/* contact */
.contact-title{left:59px;top:832px;font-weight:800;font-size:25px;line-height:30px}
.field{background:var(--navy-field);font-size:6.6px;color:var(--white);padding:0 10px;display:flex;align-items:center}
.field.message{align-items:flex-start;padding-top:10px}
.btn-submit{left:60px;top:1081px;width:62px;height:16px;background:var(--blue);font-weight:700;font-size:7.2px;display:flex;align-items:center;justify-content:center}

/* testimonials */
.bubble{left:411px;top:823px}
.testi-title{left:400px;top:919px;font-weight:800;font-size:25px;line-height:30px}
.testi-text{left:403px;top:966px;width:232px;font-size:6.6px;line-height:7.7px}
.dots{left:445px;top:1037px;display:flex;gap:9px}
.dots span{width:10px;height:10px;border-radius:50%;background:var(--navy-dot)}
.dots span.on{background:var(--blue)}

.footer-band{left:0;top:1148px;width:720px;height:52px;background:var(--blue)}
</style>
</head>
<body>

<header>
  <div class="abs brand"><span class="brand-square"></span><span class="brand-name">Kelvane Consulting</span></div>
  <nav class="abs nav">
    <a class="active" href="#">HOME</a>
    <a href="#">ABOUT US</a>
    <a href="#">SERVICES</a>
    <a href="#">CONTACT US</a>
  </nav>
</header>

<section class="hero">
  <div class="abs hero-photo" role="img" aria-label="Photo of a smiling businessman in a suit talking on a phone"></div>
  <h1 class="abs hero-title">Helping your finance<br>team and increasing<br>profit</h1>
  <a class="abs btn-outline">CONTACT US</a>
</section>

<div class="abs desk-band" role="img" aria-label="Faded photo of hands working over financial charts"></div>

<section class="services">
  <div class="abs service featured" style="left:59px">
    <svg viewBox="0 0 20 22" width="20"><path d="M2 1h11l5 5v15H2z M13 1v5h5" fill="none" stroke="#fff" stroke-width="1.6" stroke-linejoin="round"/></svg>
    <h3>Financial Models<br>– Projects</h3>
    <p>Financial analysis, scenario modeling, pricing analysis, projects</p>
  </div>
  <div class="abs service" style="left:180px">
    <svg viewBox="0 0 14 22" width="14"><text x="0" y="19" font-family="Poppins,sans-serif" font-weight="700" font-size="22" fill="#fff">$</text></svg>
    <h3>Budgeting<br>Process:</h3>
    <p>Building budgets from scratch, revamping current process to be more robust and scalable.</p>
  </div>
  <div class="abs service" style="left:303px">
    <svg viewBox="0 0 28 22" width="28"><circle cx="9" cy="5" r="4.5" fill="#fff"/><circle cx="19" cy="5" r="4.5" fill="#fff"/><path d="M0 21c0-6 4-10 9-10s8 3 8 10z M13 21c0-4 2-10 6-10 5 0 9 4 9 10z" fill="#fff"/></svg>
    <h3>Temporary<br>Staffing:</h3>
    <p>Years of Financial Planning and Analysis experience across multiple industries can help temporary staffing needs.</p>
  </div>
  <div class="abs service" style="left:425px">
    <svg viewBox="0 0 22 22" width="22"><circle cx="13" cy="9" r="7" fill="none" stroke="#fff" stroke-width="2.4"/><path d="M8 14L2 20" stroke="#fff" stroke-width="2.8" stroke-linecap="round"/></svg>
    <h3>Data<br>Cleansing</h3>
    <p>Process of identifying, correcting, and removing errors, inconsistencies, inaccuracies, and duplications in financial data</p>
  </div>
  <div class="abs service" style="left:547px">
    <svg viewBox="0 0 30 22" width="30"><path d="M1 19l9-9 5 5 11-11" fill="none" stroke="#fff" stroke-width="2.6" stroke-linejoin="round"/><path d="M19 3h9v9" fill="none" stroke="#fff" stroke-width="2.6"/></svg>
    <h3>Process<br>Improvement</h3>
    <p>Month end close, reporting, budgeting</p>
  </div>
</section>

<section class="about">
  <div class="abs about-photo" role="img" aria-label="Photo of a businessman seated in an armchair by an office window"></div>
  <div class="abs about-panel"></div>
  <h2 class="abs about-title">ABOUT US</h2>
  <p class="abs about-text">I am an experienced Finance professional who develops strategic financial plans, provides insightful analysis, and supports decision-making. With over 10 years of experience, I have successfully increased profitability for clients by $17M.</p>
  <a class="abs btn-dark">READ MORE</a>
  <div class="abs about-illustration" role="img" aria-label="Illustration of an analyst at a laptop beside a pie chart and rising bar chart"></div>
</section>

<section class="contact">
  <h2 class="abs contact-title">CONTACT US</h2>
  <div class="abs field" style="left:59px;top:882px;width:150px;height:26px">Your name</div>
  <div class="abs field" style="left:214px;top:882px;width:150px;height:26px">Your surname</div>
  <div class="abs field" style="left:59px;top:920px;width:305px;height:26px">Your email</div>
  <div class="abs field message" style="left:59px;top:958px;width:306px;height:113px">Message</div>
  <a class="abs btn-submit">SUBMIT</a>
</section>

<section class="testimonials">
  <svg class="abs bubble" width="106" height="86" viewBox="0 0 106 86"><path d="M8 0h90a8 8 0 0 1 8 8v46a8 8 0 0 1-8 8H48L32 85 28 62H8a8 8 0 0 1-8-8V8a8 8 0 0 1 8-8z" fill="#fff"/></svg>
  <h2 class="abs testi-title">TESTIMONIALS</h2>
  <p class="abs testi-text">Lorem ipsum dolor sit amet, consectetur adipiscing elit, sed do eiusmod tempor incididunt ut labore et dolore magna aliqua. Ut enim ad minim veniam, quis nostrud exercitation ullamco laboris nisi ut aliquip ex ea commodo consequat. Duis aute irure dolor in reprehenderit in voluptate velit esse cillum dolore eu fugiat nulla pariatur. Excepteur sint occaecat cupidatat non proident, sunt in culpa qui officia deserunt mollit anim id est laborum.</p>
  <div class="abs dots"><span></span><span class="on"></span><span></span><span></span><span></span><span></span><span></span><span></span></div>
</section>

<footer class="abs footer-band"></footer>

</body>
</html>
```